Business card for a "family office" company

Please provide professional looking business card designs, incorporating the attached logo and below details. Harrowmere Holdings Pty Ltd is a family office / financial investment company. We are looking for a modern, professional and contemporary card design.

Industry/Entity Type

Finance

Contact Information for Business Card

Name: Dean Mollick
Title: Director
Company: Harrowmere Holdings Pty Ltd
Email: harrowdean@quillnet.example
Mobile: 0462 735 418
Address: 4/312 Barnaby Parade, Cottesloe WA 6011, Australia

Requirements
Must have
• All details above and the logo. logo only on back side. incorporate colours of logo
Nice to have
• up to you
Should not have
• ?

```html
<!DOCTYPE html>
<html lang="en">
<head>
<meta charset="utf-8">
<title>Harrowmere Holdings – Business Card</title>
<link rel="stylesheet" href="https://fonts.googleapis.com/css2?family=Montserrat:wght@400;700&display=swap">
<style>
  :root {
    --page: #ffffff;
    --navy: #1f1f55;
    --band: #2b388f;
    --ink: #ffffff;
  }
  html, body {
    margin: 0;
    padding: 0;
    width: 1200px;
    height: 1000px;
    overflow: hidden;
    background: var(--page);
  }
  .canvas {
    position: relative;
    width: 1200px;
    height: 1000px;
    font-family: "Montserrat", Arial, sans-serif;
    color: var(--ink);
  }
  .card {
    position: absolute;
    left: 316px;
    width: 568px;
    height: 328px;
    background: var(--navy);
    overflow: hidden;
  }
  .card--front { top: 158px; }
  .card--back  { top: 514px; }

  .band {
    position: absolute;
    top: 112px;
    height: 98px;
    background: var(--band);
  }
  .band--person  { left: 0; width: 206px; }
  .band--company { left: 211px; right: 0; }

  .person {
    position: absolute;
    left: 74px;
    top: 132px;
    line-height: 20px;
  }
  .person__name {
    font-weight: 700;
    font-size: 17px;
    margin: 0;
  }
  .person__title {
    font-size: 15px;
    margin: 0;
  }

  .contact {
    position: absolute;
    left: 252px;
    top: 131px;
    font-size: 15.5px;
    line-height: 19.5px;
  }
  .contact p { margin: 0; }
  .contact__company { font-weight: 700; }

  .address {
    position: absolute;
    left: 74px;
    top: 274px;
    margin: 0;
    font-size: 15px;
  }

  .brand {
    position: absolute;
    left: 0;
    right: 0;
    top: 140px;
    display: flex;
    align-items: center;
    justify-content: center;
    gap: 14px;
  }
  .brand__mark {
    width: 22px;
    height: 22px;
    background: var(--ink);
  }
  .brand__name {
    font-weight: 400;
    font-size: 28px;
    letter-spacing: 3px;
    text-transform: uppercase;
  }
</style>
</head>
<body>
  <main class="canvas">
    <section class="card card--front" aria-label="Business card front">
      <div class="band band--person"></div>
      <div class="band band--company"></div>

      <div class="person">
        <p class="person__name">Dean Mollick</p>
        <p class="person__title">Director</p>
      </div>

      <div class="contact">
        <p class="contact__company">Harrowmere Holdings Pty Ltd</p>
        <p>E: harrowdean@quillnet.example</p>
        <p>M: 0462 735 418</p>
      </div>

      <p class="address">4/312 Barnaby Parade, Cottesloe WA 6011, Australia</p>
    </section>

    <section class="card card--back" aria-label="Business card back">
      <div class="brand">
        <span class="brand__mark" aria-hidden="true"></span>
        <span class="brand__name">Harrowmere Holdings</span>
      </div>
    </section>
  </main>
</body>
</html>
```